Product packaging for Horse related products

Hi :)

I am launching a new product for my brand, and would like some nice packaging. The product is show jumping flags for horses and as per the photos - 1 white and 1 red flag, with clips. (These are the flags that go on the side of a jump to tell the rider which way to jump over it :) )

The brand is "Maple Hollow Equestrian", and we want to be representing quality, premium products.

The packaging will obviously need our logo (attached), and a barcode on the back (can provide when finalised). In terms of the actual packaging, it has to hold the 2 plastic flags, as well as 2 smaller clips, so it needs to be secure enough to ensure bits don't drop out.

I don't mind the specific packaging product. Boxes, or calico bags or something else.. I am open to creative ideas. As long as it looks clean, nice, not too busy.

Thank you :)

Target Market(s)

Horse owners and enthusiasts

Requirements
Must have
• Packaging to safely store product and small accessories.
• logo
• Clean design (not too busy)
• Packaging dimensions
• 21.5cm wide
• 28.5 cm tall.
• Box or package will be quite flat/thin
• Box labelled as "Jump Flags"

```html
<!DOCTYPE html>
<html lang="en">
<head>
<meta charset="UTF-8">
<title>Show Jumping Flags – Packaging Front</title>
<link href="https://fonts.googleapis.com/css2?family=Montserrat:wght@300;400;500;700&display=swap" rel="stylesheet">
<style>
  :root {
    --page-bg: #ffffff;
    --box-bg: #e7e7e7;
    --band-grey: #7b7b7b;
    --pole-black: #151515;
    --pole-light: #c8d1d9;
    --pole-red: #cf2a1f;
    --ink: #1e1e1e;
    --white: #ffffff;
    --photo-light: #dcdcdc;
    --photo-mid: #9a9a9a;
    --photo-dark: #3c3c3c;
  }
  * { margin: 0; padding: 0; box-sizing: border-box; }
  html, body {
    width: 1200px;
    height: 1200px;
    overflow: hidden;
    background: var(--page-bg);
    font-family: 'Montserrat', sans-serif;
  }
  .box-front {
    position: absolute;
    left: 230px;
    top: 70px;
    width: 740px;
    height: 1060px;
    background: var(--box-bg);
    overflow: hidden;
  }
  .hero-photo {
    position: absolute;
    left: 0;
    top: 0;
    width: 700px;
    height: 410px;
    background: radial-gradient(ellipse at 55% 45%, var(--photo-mid) 0%, var(--photo-light) 70%, var(--box-bg) 100%);
  }
  .hero-photo::after {
    content: "";
    position: absolute;
    left: 0;
    top: 0;
    width: 160px;
    height: 410px;
    background: linear-gradient(90deg, var(--photo-dark), rgba(60,60,60,0));
  }
  .brand-name {
    position: absolute;
    left: 380px;
    top: 445px;
    width: 300px;
    color: var(--ink);
    font-weight: 500;
    line-height: 1.1;
  }
  .brand-name .line-main {
    display: block;
    font-size: 30px;
    letter-spacing: 0.5px;
  }
  .brand-name .line-sub {
    display: block;
    font-size: 18px;
    letter-spacing: 1px;
  }
  .jump-pole {
    position: absolute;
    left: 0;
    width: 740px;
    height: 24px;
    display: flex;
  }
  .jump-pole span { flex: 1; }
  .jump-pole .seg-black { background: var(--pole-black); }
  .jump-pole .seg-light { background: var(--pole-light); }
  .jump-pole .seg-red { background: var(--pole-red); }
  .pole-top { top: 572px; }
  .pole-bottom { top: 878px; }
  .title-band {
    position: absolute;
    left: 0;
    top: 596px;
    width: 740px;
    height: 282px;
    background: var(--band-grey);
    color: var(--white);
    text-align: center;
  }
  .title-main {
    position: absolute;
    top: 78px;
    width: 100%;
    font-size: 62px;
    font-weight: 700;
    letter-spacing: 0.5px;
  }
  .title-sub {
    position: absolute;
    top: 160px;
    width: 100%;
    font-size: 48px;
    font-weight: 300;
    letter-spacing: 14px;
    padding-left: 14px;
  }
  .contents-note {
    position: absolute;
    top: 964px;
    width: 100%;
    text-align: center;
    font-size: 20px;
    font-weight: 400;
    color: var(--ink);
  }
</style>
</head>
<body>
  <div class="box-front">
    <div class="hero-photo" role="img" aria-label="Photograph of a dapple grey horse with a rider in mid-jump"></div>

    <div class="brand-name">
      <span class="line-main">MAPLE HOLLOW</span>
      <span class="line-sub">EQUESTRIAN</span>
    </div>

    <div class="jump-pole pole-top">
      <span class="seg-black"></span><span class="seg-light"></span><span class="seg-red"></span><span class="seg-light"></span><span class="seg-black"></span>
    </div>

    <div class="title-band">
      <h1 class="title-main">SHOW JUMPING</h1>
      <h2 class="title-sub">FLAGS</h2>
    </div>

    <div class="jump-pole pole-bottom">
      <span class="seg-black"></span><span class="seg-light"></span><span class="seg-red"></span><span class="seg-light"></span><span class="seg-black"></span>
    </div>

    <p class="contents-note">Box contains: 2 plastic flags and 2 smaller clips</p>
  </div>
</body>
</html>
```